A 24' X 36" SIGN TO ANNOUNCE "ORDER YOUR TURKEY EARLY"

MUST INCLUDE OUR LOGO(PROVIDED), black background, TEXT to include
all natural
farm raised
no hormones

The sign needs to be designed for vertical(portrait) viewing. The logo needs to be smaller and emphasis on TURKEY

Farm

```html
<!DOCTYPE html>
<html lang="en">
<head>
<meta charset="utf-8">
<title>Order Your Turkey Early – Hartwell Market</title>
<link href="https://fonts.googleapis.com/css2?family=Patua+One&display=swap" rel="stylesheet">
<style>
  :root {
    --backdrop: #e6e6e6;
    --sign-black: #000000;
    --gold: #f7e11a;
    --frame-gold: #c9b21a;
    --outline-grey: #b4b4c2;
    --ornament-white: #f4f4f4;
    --roast-orange: #f19b45;
    --roast-deep: #c8692a;
    --platter-green: #7fae4a;
  }
  * { margin: 0; padding: 0; box-sizing: border-box; }
  html, body {
    width: 943px; height: 1200px; overflow: hidden;
    background: var(--backdrop);
  }
  .sign {
    position: absolute; left: 71px; top: 0;
    width: 800px; height: 1200px;
    background: var(--sign-black);
  }
  .sign-frame {
    position: absolute; left: 21px; top: 19px; right: 21px; bottom: 19px;
    border: 2px solid var(--frame-gold);
  }
  .brand-name {
    position: absolute; top: 112px; left: 0; right: 0;
    text-align: center;
    font-family: "Patua One", serif;
    font-size: 30px; line-height: 1; letter-spacing: 3px;
    color: var(--gold);
  }
  .headline-group { font-weight: normal; }
  .headline {
    position: absolute; left: 0; right: 0;
    display: block;
    text-align: center;
    font-family: "Patua One", serif;
    color: var(--gold);
    line-height: 1;
    white-space: nowrap;
  }
  .headline--order { top: 206px; font-size: 88px; letter-spacing: 1px; }
  .headline--turkey {
    top: 288px; font-size: 128px; letter-spacing: 2px;
    -webkit-text-stroke: 4px var(--outline-grey);
    paint-order: stroke fill;
  }
  .headline--early { top: 418px; font-size: 88px; letter-spacing: 1px; }
  .feature-art {
    position: absolute; left: 71px; top: 528px;
    width: 640px; height: 382px;
    border-radius: 40px;
    background:
      radial-gradient(ellipse 60% 55% at 55% 42%, var(--roast-orange) 0%, var(--roast-deep) 55%, rgba(0,0,0,0) 100%),
      radial-gradient(ellipse 75% 22% at 50% 88%, var(--platter-green) 0%, rgba(0,0,0,0) 100%);
  }
  .benefits {
    position: absolute; top: 942px; left: 0; right: 0;
    list-style: none;
  }
  .benefit {
    position: relative; height: 70px;
  }
  .benefit-text {
    position: absolute; left: 0; right: 0; top: 12px;
    text-align: center;
    font-family: "Patua One", serif;
    font-size: 56px; line-height: 1; letter-spacing: 1px;
    color: var(--gold);
  }
  .benefit-flourish {
    position: absolute; top: 24px;
    width: 46px; height: 22px; border-radius: 11px;
    background: var(--ornament-white);
  }
  .benefit-flourish--left { left: 126px; }
  .benefit-flourish--right { left: 628px; }
</style>
</head>
<body>
  <main class="sign">
    <div class="sign-frame"></div>
    <div class="brand-name">HARTWELL MARKET</div>
    <h1 class="headline-group">
      <span class="headline headline--order">ORDER YOUR</span>
      <span class="headline headline--turkey">TURKEY</span>
      <span class="headline headline--early">EARLY</span>
    </h1>
    <div class="feature-art" role="img" aria-label="Illustration of a golden roast turkey on a platter with greens and red apples"></div>
    <ul class="benefits">
      <li class="benefit">
        <span class="benefit-flourish benefit-flourish--left" role="img" aria-label="Decorative flourish"></span>
        <span class="benefit-text">ALL NATURAL</span>
        <span class="benefit-flourish benefit-flourish--right" role="img" aria-label="Decorative flourish"></span>
      </li>
      <li class="benefit">
        <span class="benefit-flourish benefit-flourish--left" role="img" aria-label="Decorative flourish"></span>
        <span class="benefit-text">FARM RAISED</span>
        <span class="benefit-flourish benefit-flourish--right" role="img" aria-label="Decorative flourish"></span>
      </li>
      <li class="benefit">
        <span class="benefit-flourish benefit-flourish--left" role="img" aria-label="Decorative flourish"></span>
        <span class="benefit-text">NO HORMONES</span>
        <span class="benefit-flourish benefit-flourish--right" role="img" aria-label="Decorative flourish"></span>
      </li>
    </ul>
  </main>
</body>
</html>
```